MARBLED SPARROW WEB DESIGN PROJECT

We are a brand new company called "Marbled Sparrow" which specialise in one-off Vintage Clothing. We would like somebody to design a web page which will be the sole income for our company. Our main aim is to have an easy searchable website which is user friendly. The key to the website is to target people who do not like the idea of op-shopping but love vintage clothes - this website will be the answer.
Updates

This website will need to be coded to work with Tin Lantern - Please read this before you start. https://help.tinlantern.example/articles/Public/How-do-I-create-custom-template-files-for-my-store

Hi everyone, Just want to make note that the this website is for young people. Just so people a clear I want modern young people dressed in Vintage clothes as this is that reality and what they would like to see. Not people dressed like they are going to a fancy dress party, i.e. dresses like it was that era. Thanks Mirela

Coding

Coded - Design and coding required

```html
<!DOCTYPE html>
<html lang="en">
<head>
<meta charset="utf-8">
<title>Marbled Sparrow – Unique Vintage Fashion and Accessories</title>
<link rel="stylesheet" href="https://fonts.googleapis.com/css2?family=Open+Sans:ital,wght@0,400;0,600;1,400&display=swap">
<style>
:root{
  --blue:#1a7aa6;
  --blue-dark:#14668c;
  --pink:#e4407a;
  --pink-text:#e0356f;
  --header-bg:#ececec;
  --cream:#f6eee4;
  --tile-frame:#d8d0c6;
  --community:#d9d9d9;
  --footer:#5b5b5b;
  --footer-low:#5e5e5e;
  --ink:#333;
  --white:#fff;
}
*{box-sizing:border-box;margin:0;padding:0}
html,body{width:1200px;height:2446px;overflow:hidden}
body{position:relative;background:var(--white);font-family:"Open Sans",Arial,sans-serif;color:var(--ink)}
.abs{position:absolute}
a{color:inherit;text-decoration:none}

/* utility bar */
.utility{top:0;left:0;width:1200px;height:49px}
.utility a{position:absolute;top:14px;font-size:14px;color:var(--pink-text);display:flex;align-items:center;gap:8px}

/* header */
.masthead{top:49px;left:0;width:1200px;height:85px;background:var(--header-bg)}
.brand{left:82px;top:16px}
.brand-name{font-size:28px;color:var(--blue);letter-spacing:1px;line-height:1}
.brand-tag{font-size:13px;color:var(--blue);margin-top:6px;word-spacing:2px}
.search{left:473px;top:24px;width:217px;height:36px;border:1px solid #9fb3bf;background:#e9eef1;display:flex;align-items:center;justify-content:space-between;padding:0 10px;font-size:10px;color:#3a5d70}
.btn-head{top:26px;height:34px;background:var(--blue);color:var(--white);font-size:15px;display:flex;align-items:center;justify-content:center}

/* nav */
.mainnav{top:134px;left:0;width:1200px;height:58px;background:var(--blue)}
.mainnav a{position:absolute;top:18px;font-size:14px;color:var(--white)}
.mainnav a.current{color:#10293a;display:flex;align-items:center;gap:10px;left:82px}
.shipping{left:880px;top:13px;width:232px;height:34px;background:var(--white);color:var(--blue);font-size:11px;line-height:13px;padding:4px 12px}

/* hero */
.hero{top:192px;left:0;width:1200px;height:555px;background:linear-gradient(100deg,#5a5c5f 0%,#a9a39a 22%,#d8c79a 45%,#c0b13c 55%,#9a4c3d 72%,#3b4f86 88%,#2b2a33 100%)}
.hero-arrow{top:445px}

/* featured */
.featured{top:787px;left:59px;width:1080px;height:432px;border:1px solid #e2e2e2;background:#fafafa}
.featured h2{position:absolute;left:23px;top:10px;font-size:24px;font-weight:400;color:#222}
.card{top:849px;width:246px;height:326px}
.card-photo{height:224px;border:1px solid #ddd;border-bottom:none}
.card-info{height:58px;background:var(--cream);text-align:center;font-size:15px;line-height:23px;padding-top:6px;color:#222}
.card-actions{display:flex;height:44px}
.card-cart{width:62px;background:var(--blue);display:flex;align-items:center;justify-content:center}
.card-more{flex:1;background:var(--pink);color:#8a1234;font-size:15px;display:flex;align-items:center;justify-content:center;gap:18px}

/* promo tiles */
.tile{top:1260px;width:330px;height:370px;border:6px solid var(--tile-frame)}
.tile-text{position:absolute;left:30px;right:22px;top:124px;font-style:italic;color:var(--white);font-size:18px;line-height:29px;word-spacing:3px}
.tile-btn{position:absolute;top:236px;left:50%;transform:translateX(-50%);width:108px;height:31px;background:#d9d6d2;color:#333;font-size:15px;display:flex;align-items:center;justify-content:center}

/* tagline */
.tagline{top:1671px;left:0;width:1200px;height:155px;background:var(--cream);display:flex;align-items:center;justify-content:center;text-align:center}
.tagline p{width:960px;font-size:20px;line-height:36px;color:#222;letter-spacing:.5px}

/* community */
.community{top:1826px;left:0;width:1200px;height:205px;background:var(--community)}
.community h3{position:absolute;left:96px;top:36px;font-size:23px;font-weight:400;color:#222}
.community .sub{position:absolute;left:94px;top:78px;font-size:15px;color:#555}
.news-input{left:93px;top:115px;width:337px;height:33px;background:var(--blue);color:var(--white);font-size:13px;padding:7px 16px}
.news-btn{left:458px;top:115px;width:109px;height:33px;background:var(--blue);color:var(--white);font-size:15px;display:flex;align-items:center;justify-content:center}
.social-title{left:874px;top:68px;font-size:23px;color:#222}
.social-list{left:874px;top:114px;width:230px;display:flex;flex-wrap:wrap;gap:6px 14px;font-size:13px;color:var(--blue-dark)}
.social-list span{display:flex;align-items:center;gap:5px}
.social-list i{width:10px;height:10px;background:var(--blue-dark);display:inline-block}

/* footer */
.footer{top:2031px;left:0;width:1200px;height:262px;background:var(--footer);color:#f1f1f1}
.fcol{top:34px}
.fcol h4{font-size:15px;font-weight:400;letter-spacing:.5px;margin-bottom:8px}
.fcol li{list-style:none;font-size:14px;line-height:24px}
.fcats{display:grid;grid-template-columns:130px 60px}
.bottom{top:2293px;left:0;width:1200px;height:153px;background:var(--footer-low);border-top:1px solid #6a6a6a}
.payments span{position:absolute;top:44px;font-size:17px;font-weight:600;color:#1d1d1d}
.copyright{position:absolute;top:98px;left:0;width:1200px;text-align:center;font-size:13px;color:#eee;letter-spacing:.5px}
</style>
</head>
<body>

<div class="abs utility">
  <a href="#" style="left:866px"><svg width="14" height="12" viewBox="0 0 14 12"><path d="M0 1h3l2 7h7l2-5H4" fill="none" stroke="currentColor" stroke-width="1.6"/><circle cx="6" cy="10.5" r="1.2" fill="currentColor"/><circle cx="11" cy="10.5" r="1.2" fill="currentColor"/></svg>View cart</a>
  <a href="#" style="left:972px"><svg width="14" height="12" viewBox="0 0 14 12" fill="currentColor"><rect x="0" y="0" width="3" height="3"/><rect x="5" y="0" width="9" height="3"/><rect x="0" y="4.5" width="3" height="3"/><rect x="5" y="4.5" width="9" height="3"/><rect x="0" y="9" width="3" height="3"/><rect x="5" y="9" width="9" height="3"/></svg>Wish list</a>
  <a href="#" style="left:1082px"><svg width="14" height="12" viewBox="0 0 14 12"><path d="M7 12L1 6C-1 3 2-1 7 3c5-4 8 0 6 3z" fill="currentColor"/></svg>Help</a>
</div>

<header class="abs masthead">
  <div class="abs brand">
    <div class="brand-name">MARBLED SPARROW</div>
    <div class="brand-tag">Unique Vintage Fashion and Accessories</div>
  </div>
  <div class="abs search"><span>search one of vintage item</span>
    <svg width="16" height="16" viewBox="0 0 16 16"><circle cx="6.5" cy="6.5" r="5" fill="none" stroke="#14668c" stroke-width="2.2"/><path d="M10 10l5 5" stroke="#14668c" stroke-width="2.6"/></svg></div>
  <a class="abs btn-head" href="#" style="left:879px;width:109px">Sign up</a>
  <a class="abs btn-head" href="#" style="left:1004px;width:108px">Login</a>
</header>

<nav class="abs mainnav">
  <a href="#" class="current"><svg width="16" height="14" viewBox="0 0 16 14" fill="#10293a"><path d="M8 0l8 7h-2v7h-4v-4H6v4H2V7H0z"/></svg>Home</a>
  <a href="#" style="left:191px">Aboutus</a>
  <a href="#" style="left:289px">Women</a>
  <a href="#" style="left:381px">Men</a>
  <a href="#" style="left:450px">Style tips</a>
  <a href="#" style="left:554px">FAQs</a>
  <a href="#" style="left:632px">Contactus</a>
  <div class="abs shipping">Orders over $100 will receive FREE shipping!</div>
</nav>

<section class="abs hero" role="img" aria-label="Smiling young woman in a yellow cardigan browsing a rail of colourful vintage clothes"></section>
<svg class="abs hero-arrow" style="left:36px" width="26" height="48" viewBox="0 0 26 48"><path d="M22 4L4 24l18 20" fill="none" stroke="#3a3a3a" stroke-width="5" opacity=".7"/></svg>
<svg class="abs hero-arrow" style="left:1138px" width="26" height="48" viewBox="0 0 26 48"><path d="M4 4l18 20L4 44" fill="none" stroke="#3a3a3a" stroke-width="5" opacity=".7"/></svg>

<section class="abs featured"><h2>Featured products</h2></section>

<article class="abs card" style="left:83px">
  <div class="card-photo" role="img" aria-label="Model in a black 1950s party dress" style="background:linear-gradient(180deg,#f4f4f4,#d9d4d0 60%,#2b2b2b 100%)"></div>
  <div class="card-info">1950s Party Dress<br>ONLY: $25</div>
  <div class="card-actions"><div class="card-cart"><svg width="28" height="24" viewBox="0 0 14 12"><path d="M0 1h3l2 7h7l2-5H4z" fill="#fff"/><circle cx="6" cy="10.5" r="1.3" fill="#fff"/><circle cx="11" cy="10.5" r="1.3" fill="#fff"/></svg></div><div class="card-more">Read More <span>&gt;&gt;</span></div></div>
</article>
<article class="abs card" style="left:346px">
  <div class="card-photo" role="img" aria-label="Rail of colourful coats and dresses" style="background:linear-gradient(90deg,#3c4f8a,#d94b6f 30%,#e3e0dc 50%,#2a2a2a 70%,#c95a8f)"></div>
  <div class="card-info">Double Breasted Coat<br>ONLY: $30</div>
  <div class="card-actions"><div class="card-cart"><svg width="28" height="24" viewBox="0 0 14 12"><path d="M0 1h3l2 7h7l2-5H4z" fill="#fff"/><circle cx="6" cy="10.5" r="1.3" fill="#fff"/><circle cx="11" cy="10.5" r="1.3" fill="#fff"/></svg></div><div class="card-more">Read More <span>&gt;&gt;</span></div></div>
</article>
<article class="abs card" style="left:608px">
  <div class="card-photo" role="img" aria-label="Model in a floral 1960s hippy dress" style="background:linear-gradient(180deg,#f4f4f4,#e6dfd8 40%,#8c2c2c 70%,#3a2020)"></div>
  <div class="card-info">1960s Hippy Dress<br>ONLY: $25</div>
  <div class="card-actions"><div class="card-cart"><svg width="28" height="24" viewBox="0 0 14 12"><path d="M0 1h3l2 7h7l2-5H4z" fill="#fff"/><circle cx="6" cy="10.5" r="1.3" fill="#fff"/><circle cx="11" cy="10.5" r="1.3" fill="#fff"/></svg></div><div class="card-more">Read More <span>&gt;&gt;</span></div></div>
</article>
<article class="abs card" style="left:872px">
  <div class="card-photo" role="img" aria-label="Colourful vintage garments on shop mannequins" style="background:linear-gradient(90deg,#4f6a35,#e7d25a 30%,#d84f5b 55%,#6aa06d 80%,#8a6b4a)"></div>
  <div class="card-info">1980s High pant<br>ONLY: $25</div>
  <div class="card-actions"><div class="card-cart"><svg width="28" height="24" viewBox="0 0 14 12"><path d="M0 1h3l2 7h7l2-5H4z" fill="#fff"/><circle cx="6" cy="10.5" r="1.3" fill="#fff"/><circle cx="11" cy="10.5" r="1.3" fill="#fff"/></svg></div><div class="card-more">Read More <span>&gt;&gt;</span></div></div>
</article>

<section class="abs tile" style="left:83px;background:linear-gradient(160deg,#6b3a2a,#4a4a44 50%,#3d5a62)" role="img" aria-label="Young woman in a knitted beanie and teal scarf outdoors">
  <p class="tile-text">"Lorem ipsum dolor sit amet, consectetur adipiscing elit, sed do eiusmod tempor inci</p>
  <a class="tile-btn" href="#">Style Tips</a>
</section>
<section class="abs tile" style="left:437px;background:linear-gradient(160deg,#5a524a,#3a3430 50%,#6a5e52)" role="img" aria-label="Young woman in a wide-brimmed black hat">
  <p class="tile-text">"Lorem ipsum dolor sit amet, consectetur adipiscing elit, sed do eiusmod tempor inci</p>
  <a class="tile-btn" href="#">Shop era</a>
</section>
<section class="abs tile" style="left:787px;background:linear-gradient(160deg,#4a3a30,#6a5444 50%,#3a2c26)" role="img" aria-label="Young woman with blonde hair resting her chin on her hand">
  <p class="tile-text">Join our VIP club and receive 5% off every Order</p>
  <a class="tile-btn" href="#">Join</a>
</section>

<section class="abs tagline"><p>******Marbled Sparrow is all about being different.That's way all of our clothes are unique, so you can be dazzling different******</p></section>

<section class="abs community">
  <h3>Become part of our community</h3>
  <p class="sub">sign up to our news letter</p>
  <div class="abs news-input">sign up for mail and update</div>
  <a class="abs news-btn" href="#">Subscribe</a>
  <div class="abs social-title">Social media</div>
  <div class="abs social-list">
    <span><i></i>Friendwall</span><span><i></i>Chirpline</span><span><i></i>Orbitly</span><span><i></i>Pinboardly</span><span><i></i>Workchain</span>
  </div>
</section>

<footer class="abs footer">
  <div class="abs fcol" style="left:197px"><h4>MARBLED SPARROW</h4><ul><li>About us</li><li>Trems of use</li><li>Privacy poilcy</li><li>Press</li></ul></div>
  <div class="abs fcol" style="left:482px;top:38px"><h4>CONNECT WITH US</h4><ul><li>Contact us</li><li>My Account</li><li>Style Tips</li><li>FAQs</li><li>Shipping</li><li>Track your order</li><li>Size cart</li></ul></div>
  <div class="abs fcol" style="left:768px;top:38px"><h4>SHOP BY POPULAR CATEGORIES</h4>
    <ul class="fcats"><li>Men</li><li>50s</li><li>Women</li><li>60s</li><li>Accessories</li><li>70s</li><li>Bags</li><li>80s</li><li>Shoes</li><li>90s</li></ul></div>
</footer>

<section class="abs bottom">
  <div class="payments">
    <span style="left:298px">SafeCert</span>
    <span style="left:473px">Payroute</span>
    <span style="left:655px">Coinpost</span>
    <span style="left:818px">Cardia</span>
  </div>
  <p class="copyright">© Marbled Sparrow. All Prices are in AUD</p>
</section>

</body>
</html>
```